Apple flavoured drink for children design art

business=flavoured drink
company name=teluvrink
address=tobel ward,Nigeria
product type=stand up pouch or doypack
product name=jolibud
sides=2 front side and back side.
favourite colour=Green
Favourite object = green apple
height=15cm
width=8cm
color=4
volume=200ml
EAN/Barcode=0847215306948

Target Market(s)

children

Industry/Entity Type

Business

Requirements
Must have
• front side
1. apple picture at the middle of the design.
2. 200ml
3. shake before drink
Back side
3. Regbod no.,PR.Date,BB. Date and Batch no. see side.
4. please keep city clean with recycle logo
5.call:0805718462
6. ingredients:water,apple cocentrste,sodium benzoate,ascorbid acid,citric acid,apple flavours
Nice to have
• write many words that will encourage the user many slogans please on the product.

```html
<!DOCTYPE html>
<html lang="en">
<head>
<meta charset="utf-8">
<title>Jolibud Apple Flavoured Drink – Pouch Front</title>
<link rel="stylesheet" href="https://fonts.googleapis.com/css2?family=Fredoka:wght@600;700&family=Passion+One:wght@700&family=Questrial&display=swap">
<style>
  :root {
    --page-bg: #ececec;
    --pouch-green: #a2c25f;
    --pouch-green-light: #c7dc9a;
    --pouch-pale: #eef2e4;
    --pouch-blush: #ede2e6;
    --brand-orange: #e9461b;
    --apple-red: #e3262b;
    --apple-outline: #2f7d26;
    --drink-maroon: #7b1112;
    --volume-green: #93b965;
    --volume-outline: #5d8a37;
    --shake-green: #3f6d21;
    --fruit-red-light: #e0566a;
    --fruit-red: #c93a4c;
    --fruit-soft: #efe9ea;
  }
  * { margin: 0; padding: 0; box-sizing: border-box; }
  html, body {
    width: 997px;
    height: 1200px;
    overflow: hidden;
    background: var(--page-bg);
  }
  .canvas {
    position: relative;
    width: 997px;
    height: 1200px;
  }
  .pouch-front {
    position: absolute;
    left: 237px;
    top: 160px;
    width: 503px;
    height: 840px;
    background: linear-gradient(
      to bottom,
      var(--pouch-green) 0%,
      var(--pouch-green) 50%,
      var(--pouch-green-light) 58%,
      var(--pouch-pale) 68%,
      #ffffff 82%,
      var(--pouch-blush) 86%,
      var(--pouch-blush) 100%
    );
    border-radius: 4px 4px 10px 10px;
  }
  .brand-name {
    position: absolute;
    top: 168px;
    left: 0;
    width: 100%;
    text-align: center;
    font-family: "Passion One", "Arial Black", sans-serif;
    font-weight: 700;
    font-size: 84px;
    line-height: 1;
    letter-spacing: 2px;
    text-transform: uppercase;
    color: var(--brand-orange);
  }
  .flavour-title {
    position: absolute;
    top: 286px;
    left: 0;
    width: 100%;
    text-align: center;
    font-family: "Fredoka", "Arial Rounded MT Bold", sans-serif;
    font-weight: 700;
    font-size: 116px;
    line-height: 1;
    letter-spacing: 1px;
    color: var(--apple-red);
    -webkit-text-stroke: 8px var(--apple-outline);
    paint-order: stroke fill;
  }
  .flavour-subtitle {
    position: absolute;
    top: 404px;
    left: 0;
    width: 100%;
    text-align: center;
    font-family: "Questrial", "Century Gothic", sans-serif;
    font-size: 38px;
    font-weight: 700;
    line-height: 1.1;
    color: var(--drink-maroon);
  }
  .fruit-visual {
    position: absolute;
    top: 470px;
    left: 46px;
    width: 412px;
    height: 244px;
    border-radius: 24px;
    background: radial-gradient(ellipse at 50% 45%, var(--fruit-red-light) 0%, var(--fruit-red) 55%, var(--fruit-soft) 100%);
  }
  .volume {
    position: absolute;
    top: 482px;
    right: 24px;
    z-index: 1;
    font-family: "Fredoka", "Arial Rounded MT Bold", sans-serif;
    font-weight: 700;
    font-size: 38px;
    line-height: 1;
    color: var(--volume-green);
    -webkit-text-stroke: 3px var(--volume-outline);
    paint-order: stroke fill;
  }
  .usage-note {
    position: absolute;
    top: 718px;
    left: 0;
    width: 100%;
    text-align: center;
    font-family: "Fredoka", "Arial Rounded MT Bold", sans-serif;
    font-weight: 600;
    font-size: 35px;
    line-height: 1;
    color: var(--shake-green);
  }
</style>
</head>
<body>
  <main class="canvas">
    <section class="pouch-front">
      <h1 class="brand-name">jolibud</h1>
      <h2 class="flavour-title">APPLE</h2>
      <p class="flavour-subtitle">flavoured drink</p>
      <div class="fruit-visual" role="img" aria-label="Photo of three ripe red apples"></div>
      <p class="volume">200ml</p>
      <p class="usage-note">shake before drink</p>
    </section>
  </main>
</body>
</html>
```